Brickline Kit - iPhone app for tradespeople - UI design

Brickline Kit is an iPhone app for tradespeople (builders, carpenters, electricians, etc) which provides a range of tools that will assist with typical tasks, such as the calculation of unit conversion and spatial/volumetric/electrical measurements. The application also makes use of instruments available in the smartphone device to provide useful tools such as a spirit level, compass and torch.

The product is a simple menu-based application consisting of a number of menu and function screens. Each menu item will navigate the user to the function screen applicable to that menu item. Each function screen will contain the necessary inputs and features for perform its stated function.

The user interface should be designed with the tradesperson user in mind and as such should be simple, intuitive and durable with respect to its usability, interface design and branding elements.

Target Market(s)

Tradespeople (builders, carpenters, electricians, etc)

Industry/Entity Type

Trade

Font styles to use
Sans Serif

Requirements
Must have
• Refer to attached wireframes document...
• - Simple design
• - Consistent layout and theme
• - Screens and icons
Should not have
• - Tacky 3D images and textured backgrounds

```html
<!DOCTYPE html>
<html lang="en">
<head>
<meta charset="utf-8">
<title>Brickline Kit – Unit Conversion Screens</title>
<link href="https://fonts.googleapis.com/css2?family=Barlow+Condensed:wght@200;300;400&display=swap" rel="stylesheet">
<style>
  :root {
    --canvas: #262626;
    --screen-dark: #141414;
    --menu-dark: #1a1a1a;
    --orange: #f39c12;
    --row-input: #f5b34a;
    --row-result: #f3a11a;
    --row-from: #e4910f;
    --row-to: #d6850c;
    --big-from: #f29c12;
    --big-from-side: #dc8a10;
    --big-to: #f7b34a;
    --big-to-side: #e4a144;
    --white: #ffffff;
    --clear-btn: rgba(255,255,255,0.3);
  }
  * { box-sizing: border-box; margin: 0; padding: 0; }
  html, body { width: 1200px; height: 745px; overflow: hidden; }
  body {
    background: var(--canvas);
    font-family: "Barlow Condensed", "Arial Narrow", sans-serif;
    font-weight: 300;
    color: var(--white);
  }
  .screens {
    display: flex;
    gap: 30px;
    padding: 52px 30px 0;
  }
  .screen {
    width: 360px;
    height: 640px;
    background: var(--screen-dark);
    display: flex;
    flex-direction: column;
    overflow: hidden;
  }
  .status-bar {
    height: 26px;
    display: flex;
    align-items: center;
    justify-content: space-between;
    padding: 0 10px;
    font-family: Arial, sans-serif;
    font-size: 10px;
    color: var(--white);
  }
  .status-bar .time { font-weight: bold; }
  .status-bar .battery { display: flex; align-items: center; gap: 4px; }
  .battery-icon {
    width: 20px; height: 9px; border: 1px solid var(--white); border-radius: 2px; padding: 1px;
  }
  .battery-icon span { display: block; width: 67%; height: 100%; background: var(--orange); }
  .app-header {
    height: 77px;
    position: relative;
    display: flex;
    align-items: center;
    justify-content: center;
  }
  .back-arrow { position: absolute; left: 20px; top: 28px; }
  .screen-title {
    color: var(--orange);
    font-size: 25px;
    font-weight: 300;
    letter-spacing: 0.5px;
  }
  .brand-name {
    color: var(--orange);
    font-size: 29px;
    font-weight: 400;
    letter-spacing: 0.5px;
  }
  .home .app-header { border-bottom: 1px solid var(--orange); }
  .hero {
    height: 288px;
    position: relative;
    background: radial-gradient(ellipse at 50% 30%, #5a5a5a 0%, #3a3a3a 45%, #222 100%);
    display: flex;
    flex-direction: column;
    align-items: center;
  }
  .hero-icon { margin-top: 70px; }
  .hero-label {
    margin-top: 22px;
    font-size: 15px;
    color: var(--orange);
    font-weight: 400;
  }
  .menu {
    flex: 1;
    background: var(--menu-dark);
    display: flex;
    flex-direction: column;
    align-items: center;
    gap: 8px;
    padding-top: 29px;
  }
  .menu-button {
    width: 293px;
    height: 59px;
    border: 1px solid var(--orange);
    display: flex;
    align-items: center;
    justify-content: center;
    color: var(--orange);
    font-size: 18px;
    font-weight: 400;
  }
  .field-row {
    height: 63px;
    display: flex;
    align-items: center;
    justify-content: space-between;
    padding: 0 26px;
    font-size: 18px;
    font-weight: 400;
  }
  .row-input { background: var(--row-input); padding-right: 16px; }
  .row-result { background: var(--row-result); }
  .row-from { background: var(--row-from); }
  .row-to { background: var(--row-to); }
  .clear-btn {
    width: 24px; height: 24px; border-radius: 50%;
    background: var(--clear-btn);
    display: flex; align-items: center; justify-content: center;
    font-family: Arial, sans-serif; font-size: 11px;
  }
  .big-row { display: flex; }
  .big-row .value {
    flex: 1;
    display: flex;
    align-items: center;
    padding-left: 26px;
    font-size: 54px;
    font-weight: 200;
  }
  .big-row .unit {
    width: 58px;
    display: flex;
    align-items: center;
    justify-content: center;
    font-size: 27px;
    font-weight: 200;
  }
  .big-from { height: 141px; background: var(--big-from); }
  .big-from .unit { background: var(--big-from-side); }
  .big-to { flex: 1; background: var(--big-to); }
  .big-to .unit { background: var(--big-to-side); }
</style>
</head>
<body>
<main class="screens">

  <!-- Home menu -->
  <section class="screen home">
    <div class="status-bar">
      <span>●●●○○ Qelvo</span><span class="time">16:05</span>
      <span class="battery">67% <span class="battery-icon"><span></span></span></span>
    </div>
    <header class="app-header">
      <svg class="back-arrow" width="24" height="18" viewBox="0 0 24 18"><path d="M23 9H2M9 1L1 9l8 8" fill="none" stroke="#f39c12" stroke-width="1.6"/></svg>
      <span class="brand-name">BRICKLINE KIT</span>
    </header>
    <div class="hero" role="img" aria-label="Blurred dark photograph of a tradesperson's workbench">
      <svg class="hero-icon" width="80" height="88" viewBox="0 0 80 88">
        <path d="M70 42 C66 28 52 22 34 24 V12 L6 30 L34 46 V36 C50 34 62 36 70 42 Z" fill="#f39c12"/>
        <path d="M10 46 C14 60 28 66 46 64 V76 L74 58 L46 42 V52 C30 54 18 52 10 46 Z" fill="#f39c12"/>
      </svg>
      <span class="hero-label">UNIT CONVERSION</span>
    </div>
    <nav class="menu">
      <div class="menu-button">Length</div>
      <div class="menu-button">Weight</div>
      <div class="menu-button">Temparature</div>
    </nav>
  </section>

  <!-- Length conversion -->
  <section class="screen converter">
    <div class="status-bar">
      <span>●●●○○ Qelvo</span><span class="time">16:05</span>
      <span class="battery">67% <span class="battery-icon"><span></span></span></span>
    </div>
    <header class="app-header">
      <svg class="back-arrow" width="24" height="18" viewBox="0 0 24 18"><path d="M23 9H2M9 1L1 9l8 8" fill="none" stroke="#f39c12" stroke-width="1.6"/></svg>
      <span class="screen-title">LENGTH</span>
    </header>
    <div class="field-row row-input"><span>20</span><span class="clear-btn">x</span></div>
    <div class="field-row row-result"><span>7.874016</span></div>
    <div class="field-row row-from"><span>Centimeters</span>
      <svg width="16" height="9" viewBox="0 0 16 9"><path d="M1 1l7 7 7-7" fill="none" stroke="#fff" stroke-width="1.5"/></svg></div>
    <div class="field-row row-to"><span>Inches</span>
      <svg width="16" height="9" viewBox="0 0 16 9"><path d="M1 1l7 7 7-7" fill="none" stroke="#fff" stroke-width="1.5"/></svg></div>
    <div class="big-row big-from"><span class="value">20</span><span class="unit">cm</span></div>
    <div class="big-row big-to"><span class="value">7.874016</span><span class="unit">in</span></div>
  </section>

  <!-- Weight conversion -->
  <section class="screen converter">
    <div class="status-bar">
      <span>●●●○○ Qelvo</span><span class="time">16:05</span>
      <span class="battery">67% <span class="battery-icon"><span></span></span></span>
    </div>
    <header class="app-header">
      <svg class="back-arrow" width="24" height="18" viewBox="0 0 24 18"><path d="M23 9H2M9 1L1 9l8 8" fill="none" stroke="#f39c12" stroke-width="1.6"/></svg>
      <span class="screen-title">WEIGHT</span>
    </header>
    <div class="field-row row-input"><span>20</span><span class="clear-btn">x</span></div>
    <div class="field-row row-result"><span>22.04620</span></div>
    <div class="field-row row-from"><span>Kilogram</span>
      <svg width="16" height="9" viewBox="0 0 16 9"><path d="M1 1l7 7 7-7" fill="none" stroke="#fff" stroke-width="1.5"/></svg></div>
    <div class="field-row row-to"><span>Pound</span>
      <svg width="16" height="9" viewBox="0 0 16 9"><path d="M1 1l7 7 7-7" fill="none" stroke="#fff" stroke-width="1.5"/></svg></div>
    <div class="big-row big-from"><span class="value">20</span><span class="unit">kg</span></div>
    <div class="big-row big-to"><span class="value">22.046200</span><span class="unit">lb</span></div>
  </section>

</main>
</body>
</html>
```